Quiet Willow Business Cards
Quiet Willow Body and Beauty Therapies
Bright & Fun-filled
Noreen Baptiste
Owner/Operator OPV, DRAM, NOPREX, VERTUMA
Bermuda
brightvanspa@examplemail.net
quietwillowvisits.com
Please design a business card with rounded corners Only the logo goes on the front. Name and additional info goes on the back Coloured background please
Noreen Baptiste (in bold print) Owner/Operator OPV, DRAM, NOPREX, VERTUMA mobile: 441-555-0148 email: brightvanspa@examplemail.net web site: quietwillowvisits.com Spa therapies in the comfort of home

```html
<!DOCTYPE html>
<html lang="en">
<head>
<meta charset="utf-8">
<title>Quiet Willow Stationery</title>
<link rel="stylesheet" href="https://fonts.googleapis.com/css2?family=Open+Sans:wght@400;600;700&display=swap">
<style>
  :root {
    --backdrop: #a6a7a6;
    --paper: #ffffff;
    --leaf-green: #5a8a3a;
    --leaf-faint: #eef1ec;
    --ink: #4a4a4a;
    --fold-line: #d9d9d9;
  }
  * { box-sizing: border-box; margin: 0; padding: 0; }
  html, body { width: 1200px; height: 684px; overflow: hidden; }
  body {
    background: var(--backdrop);
    font-family: "Open Sans", Arial, sans-serif;
    position: relative;
  }
  .sheet {
    position: absolute;
    background: var(--paper);
    box-shadow: 0 1px 3px rgba(0,0,0,.25);
  }

  /* wordmark */
  .wordmark { text-align: center; color: var(--leaf-green); line-height: 1; }
  .wordmark__name { font-weight: 600; display: inline-flex; align-items: center; gap: 6px; }
  .wordmark__dot { display: inline-block; border-radius: 50%; background: currentColor; }
  .wordmark__tagline { font-size: 7px; margin-top: 3px; letter-spacing: .3px; }

  .contact-band {
    position: absolute; left: 0; right: 0;
    background: var(--leaf-green);
    color: var(--paper);
    font-size: 6.5px;
    display: flex; align-items: center; justify-content: center;
    letter-spacing: .2px;
    white-space: nowrap;
  }

  /* letterhead */
  .letterhead { left: 192px; top: 24px; width: 470px; height: 624px; }
  .letterhead .wordmark { position: absolute; top: 50px; left: 0; right: 0; }
  .letterhead .wordmark__name { font-size: 19px; }
  .letterhead .wordmark__dot { width: 10px; height: 10px; }
  .letterhead__watermark {
    position: absolute; left: 150px; top: 200px; width: 170px; height: 200px;
    background: var(--leaf-faint); border-radius: 50%;
  }
  .letterhead .contact-band { bottom: 16px; height: 18px; }

  /* envelope back */
  .envelope-back { left: 648px; top: 60px; width: 528px; height: 271px; }
  .envelope-back__flap { position: absolute; inset: 0; }
  .envelope-back .wordmark { position: absolute; top: 128px; left: 0; right: 0; }
  .envelope-back .wordmark__name { font-size: 13px; }
  .envelope-back .wordmark__dot { width: 7px; height: 7px; }

  /* envelope front */
  .envelope-front { left: 648px; top: 372px; width: 528px; height: 223px; }
  .envelope-front .wordmark { position: absolute; top: 30px; left: 0; right: 0; }
  .envelope-front .wordmark__name { font-size: 19px; }
  .envelope-front .wordmark__dot { width: 10px; height: 10px; }
  .envelope-front .contact-band { bottom: 20px; height: 18px; }

  /* business cards */
  .card { position: absolute; left: 67px; width: 197px; border-radius: 10px; overflow: hidden; }
  .card--front {
    top: 240px; height: 127px;
    background: var(--leaf-green);
    display: flex; align-items: center; justify-content: center;
  }
  .card--front .wordmark { color: var(--paper); }
  .card--front .wordmark__name { font-size: 24px; }
  .card--front .wordmark__dot { width: 12px; height: 12px; }
  .card--front .wordmark__tagline { font-size: 8.5px; }
  .card--back {
    top: 372px; height: 108px;
    background: var(--paper);
    box-shadow: 0 1px 3px rgba(0,0,0,.25);
  }
  .card--back .wordmark { position: absolute; top: 10px; left: 0; right: 0; }
  .card--back .wordmark__name { font-size: 13px; }
  .card--back .wordmark__dot { width: 7px; height: 7px; }
  .card--back .wordmark__tagline { font-size: 5px; }
  .card__title-band {
    position: absolute; left: 0; right: 0; top: 48px; height: 10px;
    background: var(--leaf-green); color: var(--paper);
    font-size: 4.6px; display: flex; align-items: center; padding-left: 8px;
    white-space: nowrap;
  }
  .card__title-band b { font-weight: 700; margin-right: 4px; }
  .card__details {
    position: absolute; left: 8px; top: 64px;
    font-size: 4.6px; line-height: 1.6; color: var(--ink);
  }
</style>
</head>
<body>

<section class="sheet letterhead">
  <div class="wordmark">
    <div class="wordmark__name"><span class="wordmark__dot"></span>Quiet Willow</div>
    <div class="wordmark__tagline">Mobile Body &amp; Beauty Therapies</div>
  </div>
  <div class="letterhead__watermark" role="img" aria-label="Faint brand emblem decoration"></div>
  <div class="contact-band">Bermuda &nbsp;|&nbsp; 441-555-0148 &nbsp;|&nbsp; brightvanspa@examplemail.net &nbsp;|&nbsp; www.quietwillowvisits.com</div>
</section>

<section class="sheet envelope-back">
  <svg class="envelope-back__flap" viewBox="0 0 528 271" aria-hidden="true">
    <polyline points="0,0 240,118 288,118 528,0" fill="none" stroke="var(--fold-line)" stroke-width="1"/>
  </svg>
  <div class="wordmark">
    <div class="wordmark__name"><span class="wordmark__dot"></span>Quiet Willow</div>
  </div>
</section>

<section class="sheet envelope-front">
  <div class="wordmark">
    <div class="wordmark__name"><span class="wordmark__dot"></span>Quiet Willow</div>
    <div class="wordmark__tagline">Mobile Body &amp; Beauty Therapies</div>
  </div>
  <div class="contact-band">Bermuda &nbsp;|&nbsp; 441-555-0148 &nbsp;|&nbsp; brightvanspa@examplemail.net &nbsp;|&nbsp; www.quietwillowvisits.com</div>
</section>

<section class="card card--front">
  <div class="wordmark">
    <div class="wordmark__name"><span class="wordmark__dot"></span>Quiet Willow</div>
    <div class="wordmark__tagline">Mobile Body &amp; Beauty Therapies</div>
  </div>
</section>

<section class="card card--back">
  <div class="wordmark">
    <div class="wordmark__name"><span class="wordmark__dot"></span>Quiet Willow</div>
    <div class="wordmark__tagline">Mobile Body &amp; Beauty Therapies</div>
  </div>
  <div class="card__title-band"><b>Noreen Baptiste</b> Owner/Operator OPV, DRAM, NOPREX, VERTUMA</div>
  <div class="card__details">
    m: 441-555-0148<br>
    e: brightvanspa@examplemail.net &nbsp; w: quietwillowvisits.com
  </div>
</section>

</body>
</html>
```